New Coffee Brand Packaging Design

We need a package design for our new coffee brand called Harkvale Coffee. Our brand mission will be displayed on the packaging (along the side or the back) and we currently have a logo that should be displayed on the front. Feel free to suggest a new logo design as you are designing the packaging if it doesn't fit with your vision. The final design should be creative and conservative. We like coffee colors (dark and light browns, white, cream, black, gold). We also like chalkboard art imagery (i.e. coffee cups, theme words from our mission, people, etc.). One famous person from West Louisville, KY is Cornelius Bray (world famous boxer and activist). If there is a way to draw his image in more of an abstract way where it doesn't infringe any patents that would be the sort of creativity we would like in the packaging. Our coffee brand prides itself on being a coffee for the people. For the average joe, working American who enjoys a good cup of coffee and a good atmosphere.

Harkvale Coffee Mission: "We aim to be a coffee company for the people. The people who have an appreciation and love for family, community and who never forget where they came from. Our coffee was born out of West Louisville, KY…a place like many others where the hearts, the minds and the wills are strong. We hope you enjoy each and every cup. Peace & Blessings."

Reason: Extending the deadline to see if there are more design ideas.

Requirements
Must have
• (On the side or on the back of the packaging) Harkvale Coffee Mission: "We aim to be a coffee company for the people. The people who have an appreciation and love for family, community and who never forget where they came from. Our coffee was born out of West Louisville, KY…a place like many others where the hearts, the minds and the wills are strong. We hope you enjoy each and every cup. Peace & Blessings."
Nice to have
• Coffee Colors: dark and light browns, white, cream, black, gold

```html
<!DOCTYPE html>
<html lang="en">
<head>
<meta charset="utf-8">
<title>Harkvale Coffee – Package Dieline</title>
<link rel="stylesheet" href="https://fonts.googleapis.com/css2?family=Oswald:wght@500;600&family=Roboto+Condensed:wght@400&family=Lobster&display=swap">
<style>
  :root {
    --page: #ffffff;
    --cream: #e8dcc4;
    --silhouette: #e4d09c;
    --red: #e8432f;
    --red-deep: #c9412c;
    --bean-brown: #5b3a29;
    --ink: #3b2b22;
    --label: #111111;
    --dieline: #8fb8e3;
  }
  * { margin: 0; padding: 0; box-sizing: border-box; }
  html, body {
    width: 1200px; height: 900px; overflow: hidden;
    background: var(--page);
  }
  .sheet { position: relative; width: 1200px; height: 900px; }

  .panel-label {
    position: absolute;
    font: 700 17px Arial, Helvetica, sans-serif;
    color: var(--label);
    text-align: center;
    width: 200px;
  }

  .panel {
    position: absolute;
    border: 1px solid var(--dieline);
    border-radius: 11px;
    overflow: hidden;
  }
  .panel--cream { background: var(--cream); }
  .panel--pattern {
    background: linear-gradient(160deg, var(--red) 0%, var(--red-deep) 55%, var(--red) 100%);
  }
  .fold-line {
    position: absolute; left: 0; right: 0; height: 1px;
    background: var(--dieline);
  }

  .front { left: 51px; top: 97px; width: 286px; height: 543px; }
  .side-left { left: 398px; top: 97px; width: 171px; height: 543px; }
  .back { left: 631px; top: 97px; width: 286px; height: 543px; }
  .side-right { left: 978px; top: 97px; width: 171px; height: 543px; }
  .bottom { left: 631px; top: 675px; width: 286px; height: 172px; }

  .boxer-silhouette {
    position: absolute; left: 44px; top: 124px; width: 242px; height: 419px;
    background: linear-gradient(180deg, var(--silhouette) 0%, #e6d4a6 100%);
    border-radius: 90px 60px 0 0;
  }

  .brand-name {
    position: absolute; left: 0; right: 0;
    font: 600 34px "Oswald", sans-serif;
    color: var(--red);
    text-align: center;
    letter-spacing: 0.5px;
  }
  .front .brand-name { top: 62px; }
  .back .brand-name { top: 62px; }

  .product-name {
    position: absolute; left: 0; right: 0; top: 383px;
    text-align: center; color: var(--ink);
  }
  .product-grade {
    font: 600 25px/30px "Oswald", sans-serif;
    color: var(--red); letter-spacing: 0.5px;
  }
  .product-blend {
    font: 400 27px/32px "Roboto Condensed", sans-serif;
    color: var(--ink);
  }
  .product-rule {
    width: 124px; height: 2px; background: var(--ink);
    margin: 12px auto 13px;
  }
  .net-weight {
    font: 400 16px "Roboto Condensed", sans-serif;
    color: var(--ink);
  }

  .mission {
    position: absolute; left: 0; right: 0; top: 147px;
    text-align: center;
    font: 400 17px/20.7px "Roboto Condensed", sans-serif;
    color: var(--ink);
  }
  .mission-title {
    font: 500 17px/20.7px "Oswald", sans-serif;
    color: var(--ink); letter-spacing: 0.3px;
  }
  .mission p + p { margin-top: 20.7px; }
  .mission em {
    font: 600 16.5px/20.7px "Oswald", sans-serif;
    font-style: normal; color: var(--red); letter-spacing: 0.2px;
  }
  .sign-off {
    position: absolute; left: 0; right: 0; top: 496px;
    text-align: center;
    font: 400 18px "Lobster", cursive;
    color: var(--red);
  }
</style>
</head>
<body>
<main class="sheet">

  <div class="panel-label" style="left:95px; top:59px;">Front</div>
  <div class="panel-label" style="left:383px; top:59px;">Side</div>
  <div class="panel-label" style="left:674px; top:59px;">Back</div>
  <div class="panel-label" style="left:966px; top:59px;">Side</div>
  <div class="panel-label" style="left:674px; top:855px;">Bottom</div>

  <section class="panel panel--cream front">
    <div class="boxer-silhouette" role="img" aria-label="Abstract silhouette of boxer Cornelius Bray in a fighting stance"></div>
    <h1 class="brand-name">Harkvale Coffee</h1>
    <div class="product-name">
      <div class="product-grade">PREMIUM</div>
      <div class="product-blend">Blend</div>
      <div class="product-rule"></div>
      <div class="net-weight">340.2 g / 12 oz.</div>
    </div>
  </section>

  <section class="panel panel--pattern side-left" role="img" aria-label="Repeating pattern of brown coffee beans on red">
    <div class="fold-line" style="top:456px;"></div>
  </section>

  <section class="panel panel--cream back">
    <h2 class="brand-name">Harkvale Coffee</h2>
    <div class="mission">
      <p><span class="mission-title">OUR MISSION:</span><br>
      <em>WE</em> aim to be a <em>COFFEE</em><br>
      <em>COMPANY</em> for the <em>PEOPLE</em>.<br>
      The people who have an<br>
      <em>APPRECIATION</em> and <em>LOVE</em> for<br>
      <em>FAMILY</em>, <em>COMMUNITY</em> and who<br>
      <em>NEVER FORGET</em> where they<br>
      came <em>FROM</em>.</p>
      <p>Our coffee was born out<br>
      of <em>WEST LOUISVILLE, KY</em><br>
      …a place like many others<br>
      where the <em>HEARTS</em>, the <em>MINDS</em><br>
      and the <em>WILLS</em> are <em>STRONG</em>.<br>
      We hope you <em>ENJOY</em><br>
      each and every cup.</p>
    </div>
    <div class="sign-off">Peace &amp; Blessings</div>
  </section>

  <section class="panel panel--pattern side-right" role="img" aria-label="Repeating pattern of brown coffee beans on red">
    <div class="fold-line" style="top:456px;"></div>
  </section>

  <section class="panel panel--pattern bottom" role="img" aria-label="Repeating pattern of brown coffee beans on red"></section>

</main>
</body>
</html>
```